Sehr bemüht, wollte unbedingt, dass ich uneingeschränkt zufrieden bin. Folgeaufträge werden jedenfalls folgen :-)
Zielgruppe
Ich bin Finanzberater und vermittle seit 28 Jahren Versicherungen, Geldanlagen und Finanzierungen. Meine Zielgruppe würde ich als „gehoben“ ansehen, viele haben leitende Positionen, sind Freiberufler, Akademiker ...
Für mich ist der ganzheitliche Beratungsansatz (alles aus einer Hand / ein Ansprechpartner für alle finanziellen Angelegenheiten) sehr wichtig, daher betreue ich viele Kunden schon 20 Jahre und länger.
Derzeit bin ich 57 Jahre alt, viele meiner Kunden in einem ähnlichen Alter. Viele meiner Kunden sind mit Versicherungen sehr gut ausgestattet, einige haben auch Wohnungseigentum (häufig mit mir finanziert).
Im jetzigen Alter ist jedenfalls Geldanlage / Vermögensplanung stark im Vordergrund und genau darauf möchte ich mein neues Visitenkartendesign ausrichten. Im Detail geht es mir um SACHWERT-Veranlagungen, weil aus meiner Sicht unfassbar viel Geld auf unverzinsten Sparkonten von der Inflation aufgefressen werden. Ziel meiner Kunden sollte es sein, mit Sachwertveranlagungen Erträge über der Inflation zu erzielen.
Ich habe laienhafte Graphiken hochgeladen, damit Sie einen ersten Eindruck bekommen.
Die Visitenkarte zeigt aus meiner sich von links nach rechts das gesamte „Kundenleben“.
Ganz links (egal ob das die Geburt oder der Einstieg ins Berufsleben ist) sind Versicherungen sehr wichtig, Der Vermögensaufbau startet ...
Wenn man auf der „Zeitachse“ Richtung Mitte geht, gehen Versicherungsthemen tendenziell zurück, Geldanlagen bleiben gleich breit / wichtig und das Finanzieren einer Immobilie könnte dazukommen.
Mit zunehmendem Alter (auf der Zeitachse weiter nach rechts) rücken Versicherungsthemen immer weiter in den Hintergrund ...
Botschaft meinerseits: Geldanlage (und hier v.a. Sachwertanlagen) sind das ganze Leben lang „gleich wichtig“ und damit kann ich Studenten genauso wie Berufstätige oder Pensionisten sehr gut ansprechen.
In Versicherungsangelegenheiten arbeite ich mit der LUPRIX GmbH ..
Aufgabenstellung
Folgende Inhalte müssen jedenfalls irgendwo auf der Visitenkarte (vorne oder hinten) zu finden sein:
Bereits bestehendes Logo
Mag. iur. Stefan Kolbeck
GF der Kolbeck & Partner GmbH
Finanzberater
Lindweg 117, 8071 Graz
Amt für HBR Graz, FN 517382k
stefan.kolbeck@kolbeckundpartner-muster.at
www.kolbeckundpartner-muster.at
BEVO 41726315 und 26850471
Abfrage BEVO: www.bevo-muster.at/vermittlerverzeichnis
Korrekter wäre es so, aber das ist halt sehr viel Text:
BEVO:
26850471 (Gewerbliche Vermögensberatung ohne Berechtigung zur Vermittlung von Lebens- und Unfallversicherungen & Berechtigung zur Tätigkeit als ungebundener Kreditvermittler)
41726315 (Versicherungsvermittlung in der Form Mehrfach-Versicherungsagent in Kooperation mit der LUPRIX GmbH
Die Visitenkarte soll eine 'typische' Größe haben, ich glaube das ist 8,5 x 5,5 cm?
Das Design sollte aufgrund der Klientel schon 'sehr gehoben' sein.
Ergänzend möchte ich erwähnen, dass ich meine Homepage und den Netzora-Banner / Header auf das neue Design anpassen möchte, vielleicht kann letzterer nach Fertigstellung der Visitenkarte bitte mit angeboten werden!?

```html
<!DOCTYPE html>
<html lang="de">
<head>
<meta charset="utf-8">
<title>Visitenkarte Kolbeck &amp; Partner</title>
<link rel="stylesheet" href="https://fonts.googleapis.com/css2?family=Montserrat:wght@400;700&family=Open+Sans:wght@700;800&display=swap">
<style>
  :root {
    --bg: #edecea;
    --card-light: #f6f6f5;
    --card-mid: #e9e9e8;
    --wine: #8c2f3b;
    --slate: #3b5a6d;
    --ink: #1e1e1e;
    --text: #333333;
  }
  * { margin: 0; padding: 0; box-sizing: border-box; }
  html, body { width: 1200px; height: 895px; overflow: hidden; background: var(--bg); }
  .stage { position: relative; width: 1200px; height: 895px; }

  .card {
    position: absolute;
    width: 560px;
    height: 362px;
    overflow: hidden;
    background:
      linear-gradient(125deg, transparent 40%, rgba(200,200,200,.25) 48%, transparent 56%),
      linear-gradient(160deg, var(--card-light) 0%, var(--card-mid) 55%, var(--card-light) 100%);
    box-shadow: 0 2px 6px rgba(0,0,0,.12);
  }
  .card-front { left: 60px; top: 470px; }
  .card-back  { left: 580px; top: 60px; }

  .chevron { position: absolute; inset: 0; width: 100%; height: 100%; }

  .brand {
    position: absolute;
    display: flex;
    align-items: center;
    gap: 8px;
    font-family: "Montserrat", sans-serif;
    font-weight: 700;
    color: var(--wine);
  }
  .brand-square { width: 18px; height: 18px; background: var(--slate); flex: none; }
  .card-front .brand { left: 22px; top: 166px; font-size: 15px; width: 130px; line-height: 1.2; }
  .card-back .brand { left: 50%; top: 70px; transform: translateX(-50%); font-size: 20px; white-space: nowrap; }

  .contact {
    position: absolute;
    left: 282px;
    top: 44px;
    font-family: "Montserrat", sans-serif;
    color: var(--text);
  }
  .contact-name { font-weight: 700; font-size: 19px; color: var(--ink); margin-bottom: 22px; }
  .contact-line { font-size: 13.5px; line-height: 25px; }
  .contact-line.email { font-size: 11.2px; letter-spacing: -.1px; }

  .register {
    position: absolute;
    left: 0; right: 0;
    top: 150px;
    text-align: center;
    font-family: "Open Sans", sans-serif;
    font-weight: 800;
    font-size: 12.5px;
    line-height: 19px;
    color: var(--ink);
  }
</style>
</head>
<body>
<main class="stage">

  <section class="card card-back" aria-label="Rückseite">
    <div class="brand"><span class="brand-square"></span>Kolbeck &amp; Partner</div>
    <p class="register">
      BEVO:<br>
      26850471 (Gewerbliche Vermögensberatung ohne Berechtigung<br>
      zur Vermittlung von Lebens- und Unfallversicherungen &amp;<br>
      Berechtigung zur Tätigkeit als ungebundener Kreditvermittler)<br>
      41726315 (Versicherungsvermittlung in der Form Mehrfach-<br>
      Versicherungsagent in Kooperation mit der LUPRIX GmbH
    </p>
  </section>

  <section class="card card-front" aria-label="Vorderseite">
    <svg class="chevron" viewBox="0 0 560 362" preserveAspectRatio="none" aria-hidden="true">
      <polygon points="207,0 286,0 235,181 162,181" fill="var(--wine)"/>
      <polygon points="162,181 235,181 286,362 207,362" fill="var(--slate)"/>
    </svg>
    <div class="brand"><span class="brand-square"></span>Kolbeck &amp; Partner</div>
    <div class="contact">
      <p class="contact-name">Mag. iur. Stefan Kolbeck</p>
      <p class="contact-line">GF der Kolbeck &amp; Partner GmbH</p>
      <p class="contact-line">Finanzberater</p>
      <p class="contact-line">Lindweg 117</p>
      <p class="contact-line">8071 Graz</p>
      <p class="contact-line">Amt für HBR Graz</p>
      <p class="contact-line">FN 517382k</p>
      <p class="contact-line email">stefan.kolbeck@kolbeckundpartner-muster.at</p>
      <p class="contact-line">www.kolbeckundpartner-muster.at</p>
    </div>
  </section>

</main>
</body>
</html>
```